Brightacre - online store for farm produce

Online store selling fresh produce (vegetables, fruits, dairy products, meat, ...) from various farmers. Every farm has its own shopping window - order page - just like a really simple web store.

Please check the attached design brief and mock-ups for further details.

Target Market(s)

People looking for fresh vegetables, fruit, meat, ... delivered from farms

Industry/Entity Type

Farming

Coding

Coded - Design and coding required

Number of Pages Required

5+ page

Font styles to use
Sans Serif

Requirements
Must have
• Custom design. Good UX/UI design, very functional.
Responsive using bootstrap 12 point grid system

```html
<!DOCTYPE html>
<html lang="en">
<head>
<meta charset="utf-8">
<title>Brightacre – Featured Farm</title>
<link rel="stylesheet" href="https://fonts.googleapis.com/css2?family=Carlito:wght@400;700&display=swap">
<style>
:root{
  --ink:#1a1a1a;
  --muted:#6f6f6f;
  --accent:#e8201a;
  --banner:#cbcbcb;
  --rule:#e4e4e4;
  --frame:#111;
  --topbar:#eff0f0;
  --footer:#dcdadb;
  --page:#ffffff;
}
*{margin:0;padding:0;box-sizing:border-box}
html,body{width:1015px;height:1200px;overflow:hidden;background:var(--page)}
body{position:relative;font-family:"Carlito",Calibri,sans-serif;color:var(--ink)}
a{color:inherit}
.abs{position:absolute}

.top-rule{left:0;top:3px;width:858px;border-top:1px solid var(--rule)}
.header-rule{left:0;top:25px;width:1000px;border-top:1px solid #f2f2f2}
.brand{left:14px;top:19px;font-size:25px;font-weight:700;color:#163d12;letter-spacing:.2px}
.page-title{left:0;width:995px;top:18px;text-align:center;font-size:22px;font-weight:400}
.search-icon{left:909px;top:21px}
.cart-count{left:937px;top:21px;width:20px;height:20px;border-radius:50%;background:#222;color:#fff;font-size:12px;font-weight:700;text-align:center;line-height:20px}
.cart-icon{left:959px;top:22px}
.scrollbar{left:1004px;top:15px;width:11px;height:497px;background:#f1f1f1}
.scrollbar::after{content:"";position:absolute;left:1px;top:0;width:9px;height:48px;background:#c9c9c9}

.shipping-banner{left:0;top:66px;width:1005px;height:57px;background:var(--banner);text-align:center;font-size:21px;line-height:57px}

.view-all{left:11px;top:158px;font-size:10px}
.sidebar-section{left:10px;top:218px;font-size:13px;color:var(--accent)}
.sidebar-group{font-size:11.5px;color:#555}
.sidebar-list{list-style:none;font-size:6.8px;line-height:13px;color:var(--muted)}
.sidebar-list a{text-decoration:underline;text-decoration-color:#b5b5b5}

.catalog-frame{left:152px;top:172px;width:747px;height:794px;border:1px solid var(--frame);border-bottom:none}
.product{position:absolute;text-align:center;font-size:7px}
.product-photo{margin:0 auto 6px}
.product-name{display:block}

.pager{left:448px;top:805px;font-size:8px;display:flex;gap:0;align-items:center}
.pager span{display:inline-block;width:11px;text-align:center}
.pager .current{width:14px;height:14px;border-radius:50%;background:#d6d6d6;line-height:14px;margin-right:-1px}
.pager .gap{color:#999;font-size:6px}

.back-to-top{left:201px;top:903px;width:646px;height:40px;background:var(--topbar);text-align:center;font-size:14px;line-height:40px}
.back-to-top svg{vertical-align:middle;margin-left:12px}

.site-footer{left:0;top:966px;width:1015px;height:234px;background:var(--footer)}
.footer-col{position:absolute;top:40px}
.footer-col h3{font-weight:400;font-size:19px;text-decoration:underline;text-decoration-thickness:1px;margin-bottom:4px}
.footer-col ul{list-style:none;font-size:15px;line-height:29.5px}
</style>
</head>
<body>
<div class="abs top-rule"></div>
<div class="abs header-rule"></div>
<div class="abs brand">Brightacre</div>
<h1 class="abs page-title" style="font-weight:400">Featured Farm</h1>
<svg class="abs search-icon" width="24" height="24" viewBox="0 0 24 24" aria-label="Search"><circle cx="10" cy="10" r="8" fill="none" stroke="#111" stroke-width="2.4"/><line x1="16" y1="16" x2="22.5" y2="22.5" stroke="#111" stroke-width="2.8" stroke-linecap="round"/></svg>
<div class="abs cart-count">0</div>
<svg class="abs cart-icon" width="22" height="20" viewBox="0 0 22 20" aria-label="Cart"><path d="M1 2h3.5l3 11h11l2-8H6" fill="none" stroke="#111" stroke-width="2.2" stroke-linejoin="round"/><circle cx="9" cy="17" r="1.8" fill="#111"/><circle cx="17" cy="17" r="1.8" fill="#111"/></svg>
<div class="abs scrollbar"></div>

<div class="abs shipping-banner">Free Shipping on Orders $20 or above</div>

<nav>
  <a class="abs view-all" href="#" style="text-decoration:none">View All</a>
  <div class="abs sidebar-section">PRODUCE</div>
  <div class="abs sidebar-group" style="left:28px;top:245px">Fruits</div>
  <ul class="abs sidebar-list" style="left:40px;top:268px">
    <li><a href="#">Apples</a></li><li><a href="#">Apricots</a></li><li><a href="#">Avacados</a></li><li><a href="#">Bananas</a></li><li><a href="#">Blueberries</a></li><li><a href="#">Grapes</a></li><li><a href="#">Grapefruit</a></li><li><a href="#">Honeydew Melon</a></li><li><a href="#">Kiwis</a></li><li><a href="#">Lemons</a></li><li><a href="#">Limes</a></li><li><a href="#">Mangoes</a></li><li><a href="#">Nectarines</a></li><li><a href="#">Oranges</a></li><li><a href="#">Passionfruit</a></li><li><a href="#">Peaches</a></li><li><a href="#">Plums</a></li><li><a href="#">Raspberries</a></li><li><a href="#">Strawberries</a></li><li><a href="#">Watermelons</a></li>
  </ul>
  <div class="abs sidebar-group" style="left:22px;top:556px">Vegetables</div>
  <ul class="abs sidebar-list" style="left:42px;top:581px">
    <li><a href="#">Artichoke</a></li><li><a href="#">Asparagus</a></li><li><a href="#">Beans</a></li><li><a href="#">Broccoli</a></li><li><a href="#">Carrots</a></li><li><a href="#">Cabbage</a></li><li><a href="#">Cauliflower</a></li><li><a href="#">Corn</a></li><li><a href="#">Cucumbers</a></li><li><a href="#">Lettuce</a></li><li><a href="#">Mushrooms</a></li><li><a href="#">Onions</a></li><li><a href="#">Peas</a></li><li><a href="#">Peppers</a></li><li><a href="#">Potatoes</a></li><li><a href="#">Sqhash</a></li>
  </ul>
</nav>

<main class="abs catalog-frame">
  <div class="product" style="left:104px;top:30px;width:110px">
    <div class="product-photo" role="img" aria-label="Photo of a red apple" style="width:94px;height:100px;border-radius:48%;background:radial-gradient(circle at 40% 35%,#f0605a,#d3161c 60%,#9c0c10)"></div>
    <span class="product-name">Delicious Apples</span>
  </div>
  <div class="product" style="left:263px;top:30px;width:190px">
    <div class="product-photo" role="img" aria-label="Photo of two green apples" style="width:156px;height:100px;border-radius:45%;background:radial-gradient(circle at 40% 40%,#b7e25a,#6dbb22 60%,#3f8a14)"></div>
    <span class="product-name">Granny Smith</span>
  </div>
  <div class="product" style="left:510px;top:30px;width:130px">
    <div class="product-photo" role="img" aria-label="Photo of a red apple" style="width:102px;height:100px;border-radius:48%;background:radial-gradient(circle at 45% 35%,#e46d6a,#b8202c 60%,#7e1220)"></div>
    <span class="product-name">Macinstosh</span>
  </div>

  <div class="product" style="left:104px;top:214px;width:110px">
    <div class="product-photo" role="img" aria-label="Photo of an apricot" style="width:100px;height:100px;border-radius:50%;background:radial-gradient(circle at 35% 35%,#ffe28a,#f6a73c 55%,#e35a22)"></div>
    <span class="product-name">Apricots</span>
  </div>
  <div class="product" style="left:300px;top:196px;width:115px">
    <div class="product-photo" role="img" aria-label="Photo of an avocado" style="width:78px;height:114px;border-radius:50% 50% 46% 46% / 60% 60% 40% 40%;background:radial-gradient(circle at 45% 40%,#5f6a4a,#2f3524 65%,#181b13)"></div>
    <span class="product-name">Avacados</span>
  </div>
  <div class="product" style="left:510px;top:182px;width:140px">
    <div class="product-photo" role="img" aria-label="Photo of a bunch of bananas" style="width:128px;height:124px;border-radius:30% 70% 55% 45%;background:linear-gradient(135deg,#f8e36a,#f1c92c 60%,#c99a1a)"></div>
    <span class="product-name">Bananas</span>
  </div>

  <div class="product" style="left:90px;top:387px;width:160px">
    <div class="product-photo" role="img" aria-label="Photo of blueberries with leaves" style="width:156px;height:116px;border-radius:45%;background:radial-gradient(circle at 40% 55%,#6d7fa6,#3c4b70 60%,#4f8a3a)"></div>
    <span class="product-name">Blueberries</span>
  </div>
</main>

<div class="abs pager" aria-label="Pages">
  <svg width="6" height="8" viewBox="0 0 6 8"><path d="M4.5 1L1.5 4l3 3" fill="none" stroke="#111" stroke-width="1.1"/></svg>
  <span style="width:14px"></span>
  <span class="current">1</span><span>2</span><span>3</span><span>4</span><span>5</span><span>6</span><span class="gap">...</span><span style="width:14px">7</span>
  <span style="width:14px"></span>
  <svg width="6" height="8" viewBox="0 0 6 8"><path d="M1.5 1l3 3-3 3" fill="none" stroke="#111" stroke-width="1.1"/></svg>
</div>

<a class="abs back-to-top" href="#" style="text-decoration:none">Back to Top<svg width="12" height="7" viewBox="0 0 12 7"><path d="M0 7L6 0l6 7z" fill="#111"/></svg></a>

<footer class="abs site-footer">
  <div class="footer-col" style="left:101px">
    <h3>Account</h3>
    <ul><li>Register</li><li>Log In</li><li>Orders</li><li>Returns</li></ul>
  </div>
  <div class="footer-col" style="left:267px">
    <h3>Assistance</h3>
    <ul><li>Customer Care</li><li>Farm Locator</li><li>Coupons</li></ul>
  </div>
  <div class="footer-col" style="left:448px">
    <h3>Company</h3>
    <ul><li>About Us</li><li>Investor Relations</li><li>Lorem Ipsum</li></ul>
  </div>
</footer>
</body>
</html>
```